Window company.

Hello,

We are a small family business located in Madrid, Spain that works nationwide to fix, change or mount the windows of your home / premises.

The group of possible clients to whom the flyer is focused ranges from 30 to 65 years, families in general who want comfort at home and extra savings every year in heating.

It must include not only graphics and a striking aesthetic in accordance with the concepts of wanting to reach / transmit the final product to the customer to sell the product.

Details to also include:

-Brief history of the company and its foundation in 2006. It will be subsequently translated into Spanish so put in words what you consider necessary so that the client stays with the concept that we are professionals.

--Specialized in exterior aluminum and PVC carpentry.

-We move to your home for a first visit and we provide the budget totally free without any commitment.

- Also payment facilities; up to 3 times, without interest.

-Contact details of the company. (WhatsApp, email, phone and location)
Open: Mon - Friday 11,00am - 9pm
Saturday: 12,00am - 7pm
Sunday: Closed

Also as a suggestion, to decide on your own, graphics of types of window openings, if you consider that anything that is striking for the client so it wonr be yet another advertising flyer.

We are open to all kinds of ideas, all of them involving marketing branding.

We are open to any type of idea and we want to stand out, the construction world is tough and we have an idea to grow, taking into account that it must not only be beautiful but commercial to attract potential customers with all kinds of purchasing power.

Thank you.

```html
<!DOCTYPE html>
<html lang="en">
<head>
<meta charset="utf-8">
<title>Lumavent Windows Flyer</title>
<link href="https://fonts.googleapis.com/css2?family=Open+Sans:wght@400;700&family=Montserrat:wght@400&family=Roboto:wght@300;500&display=swap" rel="stylesheet">
<style>
  :root {
    --stage: #cccccc;
    --paper: #ffffff;
    --brand-red: #d21f43;
    --brand-red-deep: #9b0f2b;
    --panel-grey: #e8e9eb;
    --ink: #1b1b1b;
    --ink-soft: #3a3a3a;
    --body-grey: #8a8a8a;
    --logo-grey: #a59d8f;
  }
  html, body { margin: 0; padding: 0; width: 1200px; height: 1200px; overflow: hidden; background: var(--stage); }
  .flyer { position: absolute; left: 176px; top: 0; width: 848px; height: 1200px; display: block; }
  .head-text { font-family: 'Open Sans', sans-serif; }
  .body-text { font-family: 'Montserrat', sans-serif; }
  .title-text { font-family: 'Roboto', sans-serif; }
</style>
</head>
<body>
<svg class="flyer" viewBox="0 0 1127 1595" xmlns="http://www.w3.org/2000/svg">
  <defs>
    <linearGradient id="redFade" x1="0" y1="0" x2="0" y2="1">
      <stop offset="0" stop-color="var(--brand-red)"/>
      <stop offset="1" stop-color="var(--brand-red-deep)"/>
    </linearGradient>
    <linearGradient id="redSide" x1="0" y1="0" x2="1" y2="0">
      <stop offset="0" stop-color="var(--brand-red)"/>
      <stop offset="1" stop-color="var(--brand-red-deep)"/>
    </linearGradient>
    <linearGradient id="silver" x1="0" y1="0" x2="1" y2="0">
      <stop offset="0" stop-color="#5a5a5e"/>
      <stop offset="0.35" stop-color="#f2f2f2"/>
      <stop offset="0.55" stop-color="#8c8c90"/>
      <stop offset="0.8" stop-color="#ffffff"/>
      <stop offset="1" stop-color="#55555a"/>
    </linearGradient>
    <linearGradient id="photoTone" x1="0" y1="0" x2="1" y2="1">
      <stop offset="0" stop-color="#9fb77a"/>
      <stop offset="0.4" stop-color="#b48a63"/>
      <stop offset="0.75" stop-color="#2f3a4f"/>
      <stop offset="1" stop-color="#d8742e"/>
    </linearGradient>
  </defs>

  <!-- sheet -->
  <rect class="sheet" width="1127" height="1595" fill="var(--paper)"/>

  <!-- header -->
  <text class="head-text brand-name" x="235" y="155" font-size="36" font-weight="700" fill="var(--logo-grey)">LUMAVENT</text>
  <text class="head-text quote-line" x="1066" y="77" font-size="40" fill="var(--brand-red)" text-anchor="end">Call us for free quote</text>
  <text class="head-text quote-phone" x="1066" y="117" font-size="38" font-weight="700" fill="var(--brand-red)" text-anchor="end">+34 611 24 58 90</text>

  <!-- lower grey panel -->
  <rect class="lower-panel" x="0" y="780" width="1127" height="720" fill="var(--panel-grey)"/>

  <!-- hero swooshes -->
  <path class="swoosh-silver-top" d="M0,385 Q480,140 1127,185 L1127,220 Q520,170 0,412 Z" fill="url(#silver)"/>
  <path class="swoosh-red-top" d="M0,412 Q520,170 1127,220 L1127,250 Q520,205 0,440 Z" fill="var(--brand-red)"/>

  <!-- hero photo -->
  <path class="hero-photo" role="img" aria-label="Photo: technician in hard hat and safety glasses fitting a glass window pane with suction lifters"
        d="M0,440 Q520,205 1127,250 L1127,880 Q850,800 557,790 L0,860 Z" fill="url(#photoTone)"/>

  <!-- lower swooshes -->
  <path class="swoosh-red-bottom" d="M557,790 Q850,800 1127,880 L1127,895 Q850,820 557,810 Z" fill="var(--brand-red)"/>
  <path class="swoosh-silver-bottom" d="M557,810 Q850,820 1127,895 L1127,930 Q850,840 557,825 Z" fill="url(#silver)"/>
  <path class="ribbon-left" d="M0,860 L82,838 L82,880 L0,906 Z" fill="url(#redSide)"/>
  <path class="ribbon-silver-left" d="M0,906 L82,880 L82,890 L0,918 Z" fill="#8c8c90"/>
  <path class="box-fold" d="M60,842 L82,762 L82,842 Z" fill="var(--brand-red-deep)"/>

  <!-- offer box -->
  <rect class="offer-box" x="82" y="762" width="475" height="708" fill="url(#redFade)"/>
  <text class="title-text offer-title" x="125" y="835" font-size="30" fill="#fff"><tspan font-weight="300">WHAT </tspan><tspan font-weight="500">WE OFFER?</tspan></text>
  <rect class="offer-rule" x="127" y="856" width="366" height="3" fill="#fff"/>
  <g class="head-text offer-list" font-size="30" font-weight="700" fill="#fff">
    <circle cx="132" cy="918" r="3"/>
    <text x="143" y="928">Specialized in exterior</text>
    <text x="143" y="964">aluminum and PVC</text>
    <text x="143" y="1000">carpentry.</text>
    <circle cx="132" cy="1064" r="3"/>
    <text x="143" y="1074">We move to your home</text>
    <text x="143" y="1110">for a first visit and we</text>
    <text x="143" y="1146">provide the budget</text>
    <text x="143" y="1182">totally free without any</text>
    <text x="143" y="1218">commitment.</text>
    <circle cx="132" cy="1282" r="3"/>
    <text x="143" y="1292">Also payment facilities;</text>
    <text x="143" y="1328">up to 3 times, without</text>
    <text x="143" y="1364">interest.</text>
  </g>

  <!-- about -->
  <text class="title-text about-title" x="616" y="953" font-size="32" fill="var(--ink-soft)"><tspan font-weight="300">WHO </tspan><tspan font-weight="500">WE ARE?</tspan></text>
  <rect class="about-rule" x="875" y="940" width="191" height="3" fill="var(--ink-soft)"/>
  <g class="body-text about-copy" font-size="20.5" fill="var(--body-grey)" letter-spacing="0.6">
    <text x="616" y="993">We are a small family business located</text>
    <text x="616" y="1019">in Madrid, Spain that works nationwide</text>
    <text x="616" y="1045">to fix, change or mount the windows of</text>
    <text x="616" y="1070">your home / premises. We are founded</text>
    <text x="616" y="1096">in 2006.</text>
    <text x="616" y="1148">We offer full service from initial contact</text>
    <text x="616" y="1174">to final fitting, making sure all projects</text>
    <text x="616" y="1200">are finished to the highest standard.</text>
  </g>
  <g class="head-text opening-hours" font-size="27">
    <text x="616" y="1268" fill="var(--ink)">Open:</text>
    <text x="699" y="1268" fill="var(--brand-red)" font-weight="700">Mon - Friday 11,00am - 9pm</text>
    <text x="697" y="1308" fill="var(--brand-red)" font-weight="700">Saturday: 12,00am - 7pm</text>
    <text x="697" y="1348" fill="var(--brand-red)" font-weight="700">Sunday: Closed</text>
  </g>

  <!-- footer band -->
  <path class="footer-edge" d="M0,1460 Q700,1440 1127,1340 L1127,1595 L0,1595 Z" fill="#fff"/>
  <path class="footer-band" d="M0,1475 Q700,1455 1127,1358 L1127,1595 L0,1595 Z" fill="url(#redSide)"/>
  <path class="icon-pin" d="M147,1497 a20,20 0 0 1 20,20 c0,16 -20,42 -20,42 c0,0 -20,-26 -20,-42 a20,20 0 0 1 20,-20 Z M147,1510 a7,7 0 1 0 0.01,0 Z" fill="var(--ink)" fill-rule="evenodd"/>
  <g class="body-text footer-address" font-family="Roboto, sans-serif" font-size="21" fill="#fff" text-anchor="middle">
    <text x="393" y="1520">Pol. Ind. Las Rosas 12 (4,210.57 mi)</text>
    <text x="393" y="1551">Valdelora, Spain 28830</text>
  </g>
  <g class="icon-phone" fill="none" stroke="var(--ink)" stroke-linecap="round">
    <path d="M712,1505 c-10,8 -8,22 6,36 c14,14 26,16 34,6 l-9,-9 l-8,5 c-6,-3 -14,-11 -17,-17 l5,-8 Z" fill="var(--ink)" stroke="none"/>
    <path d="M728,1505 a16,16 0 0 1 14,14" stroke-width="3.5"/>
    <path d="M731,1494 a27,27 0 0 1 22,22" stroke-width="3.5"/>
  </g>
  <text class="head-text footer-phone" x="776" y="1535" font-size="36" font-weight="700" fill="#fff">+34 611 24 58 90</text>
</svg>
</body>
</html>
```